Web design for our new company

We need a web design for our product and for our company.
And the main is our Product tool called "veltor".
----------------------------------------------------------
[Our company's Goal]
Make organization’s communication smooth and healthy with transparency and efficiency for works and tasks in all levels with our workflow tool.

[Our Mission]
Our mission is to achieve business goals with customers.
We work together to identify the goals for your company, guides your strategy and bring the technology answers which best fit to achieve the goals.

[What we do]
We have a workflow tool "veltor"
- Very simple end-user configurable workflow for any company processes
(Targeting small-med size company)
- Graphical & fun features for startup users
- Simple and easy task control with outlook e-mail look & feel
- Non charged skill up guidance
- Additional features with;
Multiple delegation
Clear status for each owner
Task owner management console with due date reminders&reporting

Others
1. System Development & Implementation Service
Our client list includes a wide variety of small to medium to major sized enterprises.
We can offer from full-scratch based development to packaged system implementation.

2. Project Management(PM) Service
We will provide end-to-end PM service with experienced PM.
Our service is not only “managing” but “leading” to bring success to achieve the goal.

3.Consultation Service

Consulting services to a wide range of fields such as creating business strategy, business process Kaizen, IT system consultation and change management.

Target Market(s)

Business to Business
Mainly to medium size - startup company

Industry/Entity Type

It Company

Coding

Coded - Design and coding required

Number of Pages Required

5+ page

Colors
0255a3
33a6d7
86cfc6
33b8a4
add136
cadf82
fbf289
fee18a
faa54b

Requirements
Must have
• We need Pages for
• Company mission
• Service Overview
• Contact
• Privacy Policy
• Terms and Conditions
• =========================
• As there were some questions, I add followings.---------
• 1. File Format
• We are going to use Amazon web services to upload finished web files.
• The finished files should be ready to use by simply replacing images and text.
• Please provide me "easy to handle" template with "sophisticated design".
• Thanks!
• 2. Multiple Languages
• We need buttons for changing language.
• We will have this translated to German, English and Japanese.
• Thank you so much!!
Nice to have
• These are current Logos and will be a next project to revise them...
• Attached Company Profile and Logo design
• 1. Company Profile
• 2. Our Company Logo
• 3. Our Product Logo -> This is most close to our image of design base.
• 4. Product Logo for PPT Header
• All just for your reference.
• ---------
• As there were some request, I added attachment as for contents for Our mission page.
Should not have
• I hope to see some unique designs.
• (Sorry please ignore my last update as I checked with our CEO.
• Bootstrap is absolutely good template.)

```html
<!DOCTYPE html>
<html lang="en">
<head>
<meta charset="utf-8">
<title>Corvena – Home</title>
<link rel="stylesheet" href="https://fonts.googleapis.com/css2?family=Comfortaa:wght@400;700&family=Montserrat:ital,wght@0,400;0,500;0,600;0,800;1,500;1,700&display=swap">
<style>
:root{
  --blue:#0255a3;
  --hero-blue:#0a78e6;
  --hero-green:#00ee55;
  --nav-dark:#0a3f6e;
  --nav-green:#0a6a3a;
  --yellow:#fbe14a;
  --icon-yellow:#f5d631;
  --soft-yellow:#f3e48a;
  --orange:#faa54b;
  --ink:#111111;
  --white:#ffffff;
  --olive:#7ea02a;
}
*{margin:0;padding:0;box-sizing:border-box}
html,body{width:1200px;height:1200px;overflow:hidden;background:var(--white)}
body{font-family:"Montserrat",sans-serif;color:var(--ink);position:relative}
.page{position:absolute;left:318px;top:0;width:563px;height:1200px}
.abs{position:absolute}

.hero{left:0;top:0;width:563px;height:317px;background:linear-gradient(100deg,var(--hero-blue) 0%,#00a8b0 50%,var(--hero-green) 100%)}
.topbar{left:0;top:0;width:563px;height:54px;background:linear-gradient(90deg,var(--nav-dark),var(--nav-green));opacity:.92}
.brand-box{left:48px;top:0;width:56px;height:88px;background:var(--white);display:flex;align-items:center;justify-content:center}
.brand-name{font-family:"Montserrat",sans-serif;font-weight:600;font-size:9.5px;color:var(--olive);writing-mode:horizontal-tb}
.nav{right:30px;top:21px;display:flex;gap:19px;font-size:7.4px;color:var(--white)}
.hero-title{left:0;width:563px;top:128px;text-align:center;font-family:"Comfortaa",sans-serif;font-weight:700;font-size:32px;letter-spacing:1px;color:var(--white)}
.mission{left:0;width:563px;top:174px;text-align:center;font-style:italic;font-weight:500;font-size:8.8px;line-height:12.8px;color:var(--white)}
.btn-yellow{left:227px;top:238px;width:108px;height:30px;background:var(--yellow);display:flex;align-items:center;justify-content:center;font-size:8.6px;font-weight:600;color:var(--ink)}

.steps{left:19px;top:316px;width:524px;height:154px;display:flex;box-shadow:0 18px 26px rgba(0,0,0,.08)}
.step{flex:1;background:var(--white);display:flex;flex-direction:column;align-items:center;padding-top:32px}
.step svg{width:60px;height:60px}
.step-label{margin-top:16px;font-weight:800;font-size:18.5px;color:var(--ink)}
.step--active{background:var(--blue)}
.step--active .step-label{color:var(--white);margin-top:14px}

.section-title{left:0;width:563px;top:520px;text-align:center;font-family:"Comfortaa",sans-serif;font-weight:700;font-size:29px}
.services{left:30px;top:594px;width:503px;display:flex;justify-content:space-between}
.service{width:140px;display:flex;flex-direction:column;align-items:center}
.service svg{width:48px;height:40px}
.service-label{margin-top:24px;font-size:8.6px;line-height:10px;color:var(--icon-yellow);text-align:center}

.banner{left:0;top:704px;width:563px;height:219px;background:linear-gradient(160deg,#2b2b2b 0%,#1a1a1a 45%,#242424 100%)}
.banner-text{left:0;width:563px;top:760px;text-align:center;font-style:italic;font-weight:700;font-size:11.8px;line-height:23px;color:var(--soft-yellow)}
.btn-blue{left:221px;top:830px;width:122px;height:31px;background:var(--blue);display:flex;align-items:center;justify-content:center;font-size:8.6px;font-weight:600;color:var(--white)}

.footer-brand{left:0;width:563px;top:975px;text-align:center;font-weight:600;font-size:18px;color:var(--olive)}
.contact{left:0;top:1031px;width:563px;height:131px;background:var(--blue);display:flex;justify-content:space-around;padding:0 10px}
.contact-item{width:150px;display:flex;flex-direction:column;align-items:center;padding-top:27px;color:var(--white);font-weight:600;font-size:8.6px;line-height:10px;text-align:center}
.contact-item svg{width:36px;height:38px;margin-bottom:17px}
.copyright{left:0;top:1162px;width:563px;height:38px;background:var(--orange);display:flex;align-items:center;justify-content:center;font-size:8.2px;font-weight:600}
</style>
</head>
<body>
<div class="page">
  <section class="abs hero"></section>
  <header class="abs topbar"></header>
  <div class="abs brand-box"><span class="brand-name">Corvena</span></div>
  <nav class="abs nav"><span>Home</span><span>About us</span><span>Pricing</span><span>Product</span><span>OverviewPolicy</span><span>Contact Us</span></nav>
  <h1 class="abs hero-title">WELCOME TO CORVENA</h1>
  <p class="abs mission">Our mission is to achieve business goals with customers.<br>We work together to identify the goals for your company, guides your strategy and<br>bring the technology answers which best fit to achieve the goals.</p>
  <a class="abs btn-yellow">Contact Us</a>

  <div class="abs steps">
    <div class="step">
      <svg viewBox="0 0 60 60" fill="none" stroke="var(--icon-yellow)" stroke-width="2">
        <rect x="22" y="4" width="18" height="11"/><path d="M31 15v9M9 24h44M9 24v9M31 24v16M53 24v9"/>
        <rect x="3" y="33" width="11" height="14"/><rect x="25" y="40" width="11" height="14"/><rect x="47" y="33" width="11" height="14"/>
      </svg>
      <div class="step-label">Plan</div>
    </div>
    <div class="step step--active">
      <svg viewBox="0 0 60 60" fill="none" stroke="#2fa6ee" stroke-width="2">
        <path d="M12 32h38a9 9 0 0 0 0-18 15 15 0 0 0-28-4 10 10 0 0 0-12 10 7 7 0 0 0 2 12z"/>
        <path d="M16 32v10M26 32v16M36 32v16M46 32v10"/>
        <circle cx="16" cy="45" r="3"/><circle cx="26" cy="51" r="3"/><circle cx="36" cy="51" r="3"/><circle cx="46" cy="45" r="3"/>
      </svg>
      <div class="step-label">Develop</div>
    </div>
    <div class="step">
      <svg viewBox="0 0 60 60" fill="none" stroke="var(--icon-yellow)" stroke-width="2">
        <path d="M56 4c-14 0-26 8-34 22l12 12c14-8 22-20 22-34z"/><circle cx="42" cy="18" r="4"/>
        <path d="M22 26l-10 2-6 8 12-2M34 38l-2 10-8 6 2-12M16 44l-8 10"/>
      </svg>
      <div class="step-label">Launch</div>
    </div>
  </div>

  <h2 class="abs section-title">What we do</h2>
  <div class="abs services">
    <div class="service">
      <svg viewBox="0 0 48 40"><rect x="2" y="2" width="32" height="24" fill="none" stroke="#000" stroke-width="3"/><path d="M12 34h14M19 26v8" stroke="#000" stroke-width="3"/><circle cx="20" cy="13" r="4" fill="#000"/><path d="M32 20l14 16M46 20L32 36" stroke="#000" stroke-width="2.5"/></svg>
      <div class="service-label">System Development &amp;<br>Implementation Service</div>
    </div>
    <div class="service">
      <svg viewBox="0 0 48 40"><rect x="12" y="2" width="34" height="26" fill="none" stroke="#000" stroke-width="3"/><rect x="18" y="7" width="10" height="13" fill="#000"/><path d="M32 20h8v-6h-4z" fill="#000"/><circle cx="10" cy="22" r="5" fill="#000"/><path d="M0 40v-8c0-4 4-6 10-6l10-2v6l-8 3v7z" fill="#000"/></svg>
      <div class="service-label">Project Management(PM)<br>Service</div>
    </div>
    <div class="service">
      <svg viewBox="0 0 48 40"><circle cx="26" cy="14" r="10" fill="#000"/><circle cx="26" cy="14" r="4" fill="#fff"/><path d="M2 26c8-4 14-2 20 2h12l-2 4H18h16l10-6 2 4-14 10H14L2 34z" fill="#000"/></svg>
      <div class="service-label">Consultation Service</div>
    </div>
  </div>

  <div class="abs banner" role="img" aria-label="Dim photo of people working at a laptop on a wooden desk"></div>
  <p class="abs banner-text">We do our best to provide professional results to you. We believe that<br>this isn't achievable through providing a small part of the service.</p>
  <a class="abs btn-blue">Contact Us Now</a>

  <div class="abs footer-brand">Corvena</div>
  <footer class="abs contact">
    <div class="contact-item">
      <svg viewBox="0 0 36 38"><path d="M18 37C8 24 6 19 6 14a12 12 0 0 1 24 0c0 5-2 10-12 23z" fill="#fff"/><circle cx="18" cy="14" r="5" fill="var(--blue)"/></svg>
      A – 4120 Falkendorf<br>Mühlweg 7
    </div>
    <div class="contact-item">
      <svg viewBox="0 0 36 38" fill="none" stroke="#fff" stroke-width="2.5"><path d="M8 6l6 6-3 4c2 5 5 8 10 10l4-3 6 6-4 5C15 34 4 22 3 10z" fill="#fff"/><path d="M20 8a10 10 0 0 1 9 9M21 2a16 16 0 0 1 14 14"/></svg>
      0 5550-318-246
    </div>
    <div class="contact-item">
      <svg viewBox="0 0 36 38" fill="none" stroke="#fff" stroke-width="2.5"><rect x="2" y="8" width="32" height="22"/><path d="M2 8l16 13 16-13M2 30l12-11M34 30L22 19"/></svg>
      info@corvena.example
    </div>
  </footer>
  <div class="abs copyright">Copyright © 2018 CORVENA</div>
</div>
</body>
</html>
```